Loyalty/Gift Card Design-

RimTallow needs a design for a loyalty card for a retail gas discount program. The card will need to fit specifications for plumvex cards cr-80 magnetic card found on www.plumvexcards.example

The way our program works is a consumer will see advertisement for our program and come to a local gas station to purchase our RimTallow Card. It will be a set price up- front, then our program/card will save consumers 15 cents per gallon on 100 gallons of fuel. Once the 100 gallons is used the customer will have the option of reloading (for another set cost) another 100 gallons on the card to receive another 15 cents off on next 100 gallons.

Key Info to Incorporate on card--
"Save 15 cents per gallon on next 100 gallons of fuel"
Never pay full price on fuel again!
"Card Valid Only At" (then a space for our stores name and address)
Brought to you by-- RimTallow Name & Logo

Target Market(s)

Consumers conscious of gas prices/ economy who are looking to save money where they can. We are looking for a design that fits "big box" theme, with very clean design.

Industry/Entity Type

Gas Station

Requirements
Must have
• Colors Red,, Blue, White--
Sell Message of Saving and Value.
Should not have
• Designs with fuel pumps

```html
<!DOCTYPE html>
<html lang="en">
<head>
<meta charset="utf-8">
<title>RimTallow Fuel Savings Card</title>
<link rel="stylesheet" href="https://fonts.googleapis.com/css2?family=Open+Sans:ital,wdth,wght@0,75..100,400..800;1,75..100,400..800&display=swap">
<style>
  :root {
    --page: #ffffff;
    --card-blue: #4656f2;
    --card-blue-light: #6a9bff;
    --ink: #111111;
    --white: #ffffff;
    --alert-red: #ff1616;
    --band-yellow: #fff21a;
    --band-edge: #e6d400;
    --brand-navy: #1b2a8f;
    --gauge-rim: #8e9298;
  }
  * { box-sizing: border-box; margin: 0; padding: 0; }
  html, body {
    width: 1200px; height: 800px; overflow: hidden;
    background: var(--page);
  }
  .card {
    position: absolute; left: 36px; top: 43px;
    width: 1131px; height: 714px;
    border-radius: 42px; overflow: hidden;
    background:
      radial-gradient(circle at 80% 55%, var(--card-blue-light) 0%, rgba(106,155,255,0.45) 30%, rgba(70,86,242,0) 62%),
      var(--card-blue);
    font-family: "Open Sans", Arial, sans-serif;
  }
  .card__offer {
    position: absolute; left: 0; right: 0; top: 38px;
    text-align: center;
    font-size: 60px; font-weight: 600; letter-spacing: 0.5px;
    color: var(--white);
    -webkit-text-stroke: 5px var(--ink);
    paint-order: stroke fill;
    z-index: 2;
  }
  .card__slogan {
    position: absolute; left: 0; right: 0; top: 154px;
    text-align: center;
    font-size: 68px; font-weight: 800; font-stretch: 75%;
    color: var(--alert-red);
    -webkit-text-stroke: 4px var(--ink);
    paint-order: stroke fill;
    text-shadow: 0 0 10px rgba(255,255,255,0.9), 0 0 4px rgba(255,255,255,0.9);
    z-index: 2;
  }
  .card__gauge {
    position: absolute; left: 741px; top: 227px;
    width: 340px; height: 340px;
    z-index: 1;
  }
  .card__valid {
    position: absolute; left: 35px; top: 436px;
    font-size: 27px; font-weight: 500; color: var(--ink);
  }
  .card__band {
    position: absolute; left: 0; top: 605px;
    width: 1131px; height: 66px;
    background: var(--band-yellow);
    border-top: 2px solid var(--band-edge);
    border-bottom: 2px solid var(--band-edge);
  }
  .card__credit {
    position: absolute; left: 18px; top: 13px;
    font-size: 27px; font-weight: 500; color: var(--ink);
  }
  .card__credit-name {
    position: absolute; left: 342px; top: 13px;
    font-size: 27px; font-style: italic; color: var(--brand-navy);
  }
  .brand {
    position: absolute; left: 646px; top: 598px;
    display: flex; align-items: center; gap: 14px;
    z-index: 2;
  }
  .brand__mark {
    width: 68px; height: 68px;
    background: var(--brand-navy);
  }
  .brand__name {
    font-size: 70px; font-weight: 700; line-height: 1;
    color: var(--brand-navy);
  }
</style>
</head>
<body>
  <main class="card">
    <h1 class="card__offer">Save .15 cents per gallon gasoline</h1>
    <h2 class="card__slogan">Never Pay Full Price on Gasoline Again!</h2>

    <svg class="card__gauge" viewBox="0 0 340 340" role="img" aria-label="Illustration of a fuel gauge with its needle pointing to full">
      <defs>
        <radialGradient id="gauge-glow" cx="50%" cy="50%" r="50%">
          <stop offset="75%" stop-color="#fffde0" stop-opacity="0.9"/>
          <stop offset="100%" stop-color="#fffde0" stop-opacity="0"/>
        </radialGradient>
        <radialGradient id="gauge-body" cx="45%" cy="40%" r="60%">
          <stop offset="0%" stop-color="#55585e"/>
          <stop offset="100%" stop-color="#1d1e21"/>
        </radialGradient>
      </defs>
      <circle cx="170" cy="170" r="170" fill="url(#gauge-glow)"/>
      <circle cx="170" cy="170" r="148" fill="var(--gauge-rim)"/>
      <circle cx="170" cy="170" r="128" fill="url(#gauge-body)"/>
    </svg>

    <p class="card__valid">Card Valid Only At :</p>

    <div class="card__band">
      <span class="card__credit">Brought to you by :</span>
      <span class="card__credit-name">RimTallow</span>
    </div>

    <div class="brand">
      <span class="brand__mark"></span>
      <span class="brand__name">RimTallow</span>
    </div>
  </main>
</body>
</html>
```